Modern book cover design

We are looking for a modern, powerful book cover for a general intrest book about how robots are going to take human jobs in the future.

The book title is "Gearfallow"

It also has a strap line "The end of human jobs and how robots will replace them"
Both the title and the strap line should be on the front cover

I have attached a number of book designs I like, and my author picture.

Reason: Some great submissions but none quite have that wow factor

Target Market(s)

This is a general intrest book, but the reader is likely to be male 30-50

Requirements
Must have
• -Title "Gearfallow"

-Strap-line "The end of human jobs and how robots will replace them"

-Be compliant with PressLoom Cover Design Criteria(www.pressloom-sample.com)

-Book size : 5.5 x 8.5 inches

-Spine size : 0.625 inches

-Must have one author picture on the back cover(attached)

-Must have the following author description on back cover:
"Tom Hardle is a leading futurologist, technologist, inventor, and entrepreneur. With over twenty years of experience in technology and innovation, Tom has travelled the world seeking out and developing new technologies. As a leading voice on the challenges and benefits of tomorrow’s technology, he has advised some of the world’s leading institutions, including the Granite Hall, regarding technological preparations for the future. He is the recipient of the harvest founder of the season prize and has appeared on numerous technology and philanthropy television programs, as well as presenting Clever Little Sparks on Robotics."

-Must have the following book description on back cover:
“Gearfallow is a look at the rapidly changing face of robotics and how it will revolutionize employment over the next thirty years. Tom Hardle lays out the arguments in favor of and against the mechanization of our society, as well as the advantages and untold risks as we march into this ever-present future.”

-Must have the following quote on the back cover:
"A fascinating look into the future of robotics and their impact on humanity, be prepared to question when robots will replace you - Simon Elstree, Professor of Cybernetics at the University of Marlowe”

-Example barcode

```html
<!DOCTYPE html>
<html lang="en">
<head>
<meta charset="utf-8">
<title>Gearfallow – Book Cover</title>
<link href="https://fonts.googleapis.com/css2?family=Open+Sans:ital,wght@0,400;0,700;1,400&family=Roboto+Condensed:wght@400;700&display=swap" rel="stylesheet">
<style>
  :root {
    --paper: #f3f3f3;
    --paper-grain: #e9e9e9;
    --ink: #111111;
    --title-red: #ee1c1c;
    --title-shadow: rgba(0, 0, 0, 0.35);
    --photo-light: #9a9a9a;
    --photo-dark: #3a3a3a;
    --button-red: #e3201b;
    --button-dark: #9e0f0c;
    --barcode-frame: #8a8a8a;
    --barcode-fill: #ffffff;
  }
  * { margin: 0; padding: 0; box-sizing: border-box; }
  html, body { width: 1200px; height: 879px; overflow: hidden; }
  body {
    background: var(--paper);
    font-family: "Open Sans", Arial, sans-serif;
    color: var(--ink);
  }
  .cover {
    position: relative;
    width: 1200px;
    height: 879px;
    background: radial-gradient(circle at 30% 40%, var(--paper) 0%, var(--paper-grain) 120%);
  }

  /* Back cover */
  .back-bio {
    position: absolute;
    left: 52px;
    top: 53px;
    width: 495px;
    font-size: 13.2px;
    line-height: 17.7px;
  }
  .author-photo {
    float: left;
    width: 130px;
    height: 154px;
    margin: 0 10px 2px 0;
    background: linear-gradient(160deg, var(--photo-light), var(--photo-dark));
  }
  .book-blurb {
    position: absolute;
    left: 53px;
    top: 352px;
    width: 490px;
    font-size: 12.4px;
    font-weight: 700;
    line-height: 22.4px;
  }
  .endorsement {
    position: absolute;
    left: 53px;
    top: 660px;
    width: 490px;
    font-size: 12.4px;
    line-height: 22px;
  }
  .endorsement-quote { font-weight: 700; }
  .endorsement-source { font-style: italic; padding-left: 51px; }
  .barcode-area {
    position: absolute;
    left: 440px;
    top: 792px;
    width: 103px;
    height: 61px;
    background: var(--barcode-fill);
    border: 1px solid var(--barcode-frame);
  }

  /* Spine */
  .spine {
    position: absolute;
    left: 558px;
    top: 640px;
    transform-origin: 0 0;
    transform: rotate(-90deg);
    white-space: nowrap;
    font-family: "Roboto Condensed", "Arial Narrow", sans-serif;
    display: flex;
    align-items: baseline;
    gap: 8px;
  }
  .spine-title {
    color: var(--title-red);
    font-weight: 700;
    font-size: 72px;
    letter-spacing: 10px;
    line-height: 1;
    text-shadow: 2px 2px 2px var(--title-shadow);
  }
  .spine-author {
    font-size: 34px;
    line-height: 1;
  }

  /* Front cover */
  .front-title {
    position: absolute;
    right: 14px;
    top: 12px;
    font-family: "Roboto Condensed", "Arial Narrow", sans-serif;
    font-weight: 700;
    font-size: 112px;
    letter-spacing: 7px;
    line-height: 1;
    color: var(--title-red);
    text-shadow: 3px 3px 3px var(--title-shadow);
  }
  .front-author {
    position: absolute;
    right: 42px;
    top: 138px;
    font-family: "Roboto Condensed", "Arial Narrow", sans-serif;
    font-size: 50px;
    line-height: 1;
    text-shadow: 2px 2px 2px rgba(0, 0, 0, 0.2);
  }
  .strapline {
    position: absolute;
    left: 630px;
    width: 555px;
    top: 647px;
    text-align: center;
    font-family: "Roboto Condensed", "Arial Narrow", sans-serif;
    font-size: 30px;
    line-height: 35px;
    text-decoration: underline;
    text-decoration-thickness: 2px;
    text-underline-offset: 4px;
    text-shadow: 1px 1px 2px rgba(0, 0, 0, 0.25);
  }
  .push-button {
    position: absolute;
    left: 1036px;
    top: 745px;
    width: 98px;
    height: 84px;
  }
</style>
</head>
<body>
<main class="cover">

  <section class="back-cover">
    <div class="back-bio">
      <div class="author-photo" role="img" aria-label="Black and white portrait photograph of author Tom Hardle"></div>
      <p>Tom Hardle is a leading futurologist, technologist, inventor, and entrepreneur. With over twenty years of experience in technology and innovation, Tom has travelled the world seeking out and developing new technologies. As a leading voice on the challenges and benefits of tomorrow’s technology, he has advised some of the world’s leading institutions, including the Granite Hall, regarding technological preparations for the future. He is the recipient of the harvest founder of the season prize and has appeared on numerous technology and philanthropy television programs, as well as presenting Clever Little Sparks on Robotics.</p>
    </div>

    <p class="book-blurb">Gearfallow is a look at the rapidly changing face of robotics and how it will revolutionize employment over the next thirty years. Tom Hardle lays out the arguments in favor of and against the mechanization of our society, as well as the advantages and untold risks as we march into this ever-present future.</p>

    <blockquote class="endorsement">
      <p class="endorsement-quote">"A fascinating look into the future of robotics and their impact on humanity, be prepared to question when robots will replace you "</p>
      <p class="endorsement-source">Simon Elstree, Professor of Cybernetics at the University of Marlowe.</p>
    </blockquote>

    <div class="barcode-area" role="img" aria-label="Reserved area for the book barcode"></div>
  </section>

  <div class="spine">
    <span class="spine-title">Gearfallow</span>
    <span class="spine-author">Tom Hardle</span>
  </div>

  <section class="front-cover">
    <h1 class="front-title">Gearfallow</h1>
    <p class="front-author">Tom Hardle</p>
    <p class="strapline">The end of human jobs and how robots will replace them.</p>

    <svg class="push-button" viewBox="0 0 98 84" aria-hidden="true">
      <defs>
        <radialGradient id="button-face" cx="45%" cy="30%" r="70%">
          <stop offset="0%" stop-color="#ff6a5e"/>
          <stop offset="55%" stop-color="#e3201b"/>
          <stop offset="100%" stop-color="#9e0f0c"/>
        </radialGradient>
        <linearGradient id="button-rim" x1="0" y1="0" x2="0" y2="1">
          <stop offset="0%" stop-color="#f2f2f2"/>
          <stop offset="100%" stop-color="#8c8c8c"/>
        </linearGradient>
      </defs>
      <ellipse cx="49" cy="56" rx="46" ry="26" fill="url(#button-rim)"/>
      <ellipse cx="49" cy="52" rx="38" ry="20" fill="#9e0f0c"/>
      <ellipse cx="49" cy="38" rx="38" ry="30" fill="url(#button-face)"/>
      <text x="49" y="34" text-anchor="middle" font-family="Roboto Condensed, Arial Narrow, sans-serif" font-weight="700" font-size="16" fill="#ffffff">PUSH</text>
    </svg>
  </section>

</main>
</body>
</html>
```